Kestrel Gardenworks Business Card

An eye catching, yet simple business card that includes;

1. our logo
2. office phone - 5083172946
3. email - kestrelgardenworks@mailbrook.com
4. website - www.kestrelgardenworks.com
5. instagram - @kestrelgardenworksnv

```html
<!DOCTYPE html>
<html lang="en">
<head>
<meta charset="utf-8">
<title>Kestrel Gardenworks Business Card</title>
<link href="https://fonts.googleapis.com/css2?family=Montserrat:wght@400;500;700;800&display=swap" rel="stylesheet">
<style>
  :root {
    --bg: #e9e5df;
    --brown: #9a5b22;
    --brown-light: #c98a48;
    --brown-dark: #5e3613;
    --ink: #1d1a18;
    --white: #ffffff;
  }
  * { margin: 0; padding: 0; box-sizing: border-box; }
  html, body { width: 1200px; height: 912px; overflow: hidden; }
  body {
    background: var(--bg);
    font-family: "Montserrat", Arial, sans-serif;
    position: relative;
  }
  .card {
    position: absolute;
    width: 600px;
    height: 343px;
    box-shadow: 0 10px 28px rgba(0,0,0,0.22);
    overflow: hidden;
  }
  .card-back { left: 60px; top: 60px; background: var(--brown); }
  .pattern-fill {
    position: absolute; inset: 0;
    background: linear-gradient(200deg, var(--brown-light) 0%, var(--brown) 50%, var(--brown-dark) 100%);
  }
  .card-front { left: 540px; top: 500px; background: var(--white); }
  .wave { position: absolute; inset: 0; }
  .brand {
    position: absolute;
    left: 30px; top: 104px;
    display: flex; align-items: center; gap: 10px;
  }
  .brand-dot {
    width: 20px; height: 20px; border-radius: 50%;
    background: var(--brown); flex: none;
  }
  .brand-name {
    color: var(--brown);
    font-weight: 800;
    font-size: 22px;
    line-height: 1.05;
    text-transform: uppercase;
  }
  .divider {
    position: absolute;
    left: 282px; top: 66px;
    width: 2px; height: 122px;
    background: var(--brown);
  }
  .details { position: absolute; left: 300px; top: 60px; }
  .person-name {
    color: var(--brown);
    font-weight: 800;
    font-size: 26px;
    letter-spacing: 0.5px;
    line-height: 1;
  }
  .person-role { color: var(--ink); font-size: 14px; margin-top: 4px; }
  .contacts { list-style: none; margin-top: 14px; }
  .contacts li {
    display: flex; align-items: center; gap: 7px;
    color: var(--ink);
    font-size: 13px;
    line-height: 21px;
    white-space: nowrap;
  }
  .contacts svg { width: 12px; height: 12px; flex: none; }
  .social {
    position: absolute;
    left: 300px; top: 204px;
    display: flex; align-items: center; gap: 7px;
    color: var(--ink); font-size: 13.5px;
  }
  .social-dot {
    width: 13px; height: 13px; border-radius: 50%;
    border: 2px solid var(--brown);
  }
</style>
</head>
<body>

  <section class="card card-back">
    <div class="pattern-fill" role="img" aria-label="Repeating pattern of leaping animal silhouettes in brown tones"></div>
  </section>

  <section class="card card-front">
    <svg class="wave" viewBox="0 0 600 343" preserveAspectRatio="none" aria-hidden="true">
      <path d="M0 343 L0 334 C220 330 430 304 600 256 L600 343 Z" fill="#9a5b22"/>
      <path d="M0 322 C220 316 430 290 600 244" fill="none" stroke="#1d1a18" stroke-width="5"/>
    </svg>

    <div class="brand">
      <span class="brand-dot"></span>
      <span class="brand-name">Kestrel<br>Gardenworks</span>
    </div>

    <div class="divider"></div>

    <div class="details">
      <div class="person-name">REID CALLOWAY</div>
      <div class="person-role">Director</div>
      <ul class="contacts">
        <li>
          <svg viewBox="0 0 24 24"><path fill="#9a5b22" d="M6.6 10.8a15.1 15.1 0 0 0 6.6 6.6l2.2-2.2c.3-.3.7-.4 1-.2 1.1.4 2.3.6 3.6.6.6 0 1 .4 1 1V20c0 .6-.4 1-1 1C10.6 21 3 13.4 3 4c0-.6.4-1 1-1h3.5c.6 0 1 .4 1 1 0 1.3.2 2.5.6 3.6.1.3 0 .7-.2 1z"/></svg>
          (508) 317 2946
        </li>
        <li>
          <svg viewBox="0 0 24 24"><rect x="2" y="5" width="20" height="14" rx="1.5" fill="none" stroke="#9a5b22" stroke-width="2.4"/><path d="M3 6l9 7 9-7" fill="none" stroke="#9a5b22" stroke-width="2.4"/></svg>
          kestrelgardenworks@mailbrook.com
        </li>
        <li>
          <svg viewBox="0 0 24 24"><circle cx="12" cy="12" r="9.5" fill="none" stroke="#9a5b22" stroke-width="2.2"/><path d="M2.5 12h19M12 2.5c3 3 3 16 0 19M12 2.5c-3 3-3 16 0 19" fill="none" stroke="#9a5b22" stroke-width="1.8"/></svg>
          www.kestrelgardenworks.com
        </li>
      </ul>
    </div>

    <div class="social">
      <span class="social-dot"></span>
      @kestrelgardenworksnv
    </div>
  </section>

</body>
</html>
```